Business cards, Stationary, E-mail signature, leterhead, fax coversheet, thank you card, invoice tem
Torvan Networks Stationary - please read brief
Business cards, Stationary, E-mail signature, leterhead, fax coversheet, thank you card, invoice tem -
Creative Brief
Use specific fonts
Use the best that will go with the logo design
Professional
Brent Oakley
71523 Birch Ridge Court, Suite 204 Sterling, VA 20783
BrentO@torvannetworks.example
www.torvannetworks.example
Use the icon on the left side of the logo only

```html
<!DOCTYPE html>
<html lang="en">
<head>
<meta charset="utf-8">
<title>Torvan Networks Stationery</title>
<link href="https://fonts.googleapis.com/css2?family=Roboto:wght@400;700&family=Great+Vibes&display=swap" rel="stylesheet">
<style>
:root{
  --bg:#e6e8eb;
  --paper:#ffffff;
  --blue:#1f56b0;
  --navy:#0e2e6a;
  --sky:#6c9be0;
  --ink:#3a3f47;
  --line:#cfd5dd;
}
*{box-sizing:border-box;margin:0;padding:0}
html,body{width:1200px;height:521px;overflow:hidden;background:var(--bg);font-family:"Roboto",Arial,sans-serif;color:var(--ink)}
.canvas{position:relative;width:1200px;height:521px}
.piece{position:absolute;background:var(--paper);box-shadow:0 2px 6px rgba(0,0,0,.25);overflow:hidden}
.brand{display:flex;align-items:center;gap:4px;color:var(--blue);font-weight:700;white-space:nowrap;line-height:1}
.brand .dot{width:1em;height:1em;border-radius:50%;background:var(--blue);flex:none}
.tiny{font-size:4.5px;line-height:1.5}
.band{position:absolute;left:0;right:0;background:linear-gradient(90deg,var(--navy),var(--blue),var(--sky))}

/* letterhead */
.letterhead{left:211px;top:43px;width:202px;height:324px}
.letterhead .brand{position:absolute;left:14px;top:14px;font-size:9px}
.letterhead .footer{position:absolute;left:0;right:0;bottom:0;height:22px;border-top:2px solid var(--blue);padding:5px 10px;display:flex;justify-content:space-between}

/* fax */
.fax{left:432px;top:43px;width:202px;height:324px}
.fax .brand{position:absolute;left:14px;top:14px;font-size:9px}
.fax .title{position:absolute;right:14px;top:16px;font-size:8px;font-weight:700;color:var(--navy)}
.fax .fields{position:absolute;left:14px;right:14px;top:44px;display:grid;grid-template-columns:1fr 1fr;gap:6px 10px}
.fax .field{border-bottom:1px solid var(--line);padding-bottom:2px}
.fax .checks{position:absolute;left:14px;right:14px;top:114px;display:flex;gap:8px}
.fax .checks span::before{content:"";display:inline-block;width:4px;height:4px;border:1px solid var(--blue);margin-right:2px;vertical-align:middle}
.fax .rule{position:absolute;left:14px;right:14px;top:126px;height:1px;background:var(--blue)}
.fax .footer{position:absolute;left:0;right:0;bottom:0;height:22px;border-top:2px solid var(--blue);padding:5px 10px;text-align:center}

/* invoice */
.invoice{left:653px;top:43px;width:202px;height:324px}
.invoice .brand{position:absolute;left:14px;top:14px;font-size:9px}
.invoice .title{position:absolute;right:14px;top:16px;font-size:8px;font-weight:700;color:var(--blue)}
.invoice .meta{position:absolute;right:14px;top:30px;text-align:right}
.invoice .from{position:absolute;left:14px;top:34px}
.invoice table{position:absolute;left:14px;top:70px;width:174px;border-collapse:collapse;font-size:4.5px}
.invoice th{background:var(--blue);color:#fff;font-weight:700;padding:2px;text-align:left}
.invoice td{border:1px solid var(--line);height:70px}
.invoice .total{position:absolute;right:14px;top:170px;width:60px;display:flex;justify-content:space-between;background:var(--navy);color:#fff;padding:2px 4px}
.invoice .footer{position:absolute;left:0;right:0;bottom:0;height:22px;border-top:2px solid var(--blue);padding:5px 10px;text-align:center}

/* thank you card */
.thanks{left:874px;top:43px;width:295px;height:168px}
.thanks .brand{position:absolute;left:18px;top:18px;font-size:16px}
.thanks .tag{position:absolute;left:44px;top:38px;color:var(--navy)}
.thanks .script{position:absolute;right:24px;top:68px;font-family:"Great Vibes",cursive;font-size:40px;color:var(--blue)}
.thanks svg{position:absolute;left:0;bottom:0}

/* business cards */
.card{width:139px;height:70px}
.card-front{left:53px;top:94px;height:46px}
.card-front .brand{position:absolute;left:8px;top:8px;font-size:8px}
.card-front .who{position:absolute;left:8px;top:22px}
.card-front .who b{font-size:5.5px;color:var(--navy)}
.card-blue{left:53px;top:142px;background:linear-gradient(135deg,var(--navy),var(--blue) 60%,var(--sky))}
.card-blue .brand{position:absolute;left:12px;top:28px;font-size:10px;color:#fff}
.card-blue .brand .dot{background:#fff}
.card-gray{left:53px;top:221px;background:linear-gradient(135deg,#8f98a4,#dfe3e8)}
.card-gray .brand{position:absolute;left:12px;top:28px;font-size:10px;color:var(--navy)}
.card-gray .brand .dot{background:var(--navy)}
.card-white{left:53px;top:355px}
.card-white .brand{position:absolute;left:12px;top:28px;font-size:10px}

/* envelope */
.envelope{left:221px;top:377px;width:408px;height:108px}
.envelope .brand{position:absolute;left:14px;top:14px;font-size:10px}
.envelope .addr{position:absolute;left:32px;top:28px}
.envelope .band{bottom:0;height:12px}
.envelope svg{position:absolute;left:0;top:0}

/* email signatures */
.sig{padding:6px 8px}
.sig .name{font-size:5.5px;font-weight:700;color:var(--navy);margin-bottom:2px}
.sig .brand{font-size:8px;margin-bottom:3px}
.sig-a{left:888px;top:235px;width:144px;height:50px}
.sig-b{left:1037px;top:240px;width:134px;height:42px}
.sig-c{left:888px;top:307px;width:144px;height:52px}
.sig-d{left:1037px;top:310px;width:134px;height:44px}
.sig-e{left:720px;top:379px;width:134px;height:68px}

/* logo panel */
.logo-panel{left:955px;top:379px;width:214px;height:108px;display:flex;align-items:center;justify-content:center}
.logo-panel .brand{font-size:18px}
</style>
</head>
<body>
<main class="canvas">

  <section class="piece card card-front">
    <div class="brand"><span class="dot"></span>Torvan Networks</div>
    <div class="who tiny"><b>Brent Oakley</b><br>Director · 555 010 2040</div>
  </section>
  <section class="piece card card-blue">
    <div class="brand"><span class="dot"></span>Torvan Networks</div>
  </section>
  <section class="piece card card-gray">
    <div class="brand"><span class="dot"></span>Torvan Networks</div>
  </section>
  <section class="piece card card-white">
    <div class="brand"><span class="dot"></span>Torvan Networks</div>
  </section>

  <section class="piece letterhead">
    <div class="brand"><span class="dot"></span>Torvan Networks</div>
    <div class="footer tiny"><span>71523 Birch Ridge Court, Suite 204</span><span>555 010 2040</span><span>www.torvannetworks.example</span></div>
  </section>

  <section class="piece fax">
    <div class="brand"><span class="dot"></span>Torvan Networks</div>
    <div class="title">FAX</div>
    <div class="fields tiny">
      <div class="field">To:</div><div class="field">From:</div>
      <div class="field">Fax:</div><div class="field">Pages:</div>
      <div class="field">Phone:</div><div class="field">Date:</div>
      <div class="field">Re:</div><div class="field">CC:</div>
    </div>
    <div class="checks tiny"><span>Urgent</span><span>For Review</span><span>Please Comment</span><span>Please Reply</span></div>
    <div class="rule"></div>
    <div class="footer tiny">71523 Birch Ridge Court, Suite 204 · Sterling, VA 20783 · www.torvannetworks.example</div>
  </section>

  <section class="piece invoice">
    <div class="brand"><span class="dot"></span>Torvan Networks</div>
    <div class="title">INVOICE</div>
    <div class="meta tiny">Date:<br>Invoice #:</div>
    <div class="from tiny">71523 Birch Ridge Court, Suite 204<br>Sterling, VA 20783</div>
    <table>
      <tr><th>Description</th><th>Qty</th><th>Price</th><th>Amount</th></tr>
      <tr><td></td><td></td><td></td><td></td></tr>
    </table>
    <div class="total tiny"><span>Total</span><span>$0.00</span></div>
    <div class="footer tiny">BrentO@torvannetworks.example · www.torvannetworks.example</div>
  </section>

  <section class="piece thanks">
    <div class="brand"><span class="dot"></span>Torvan Networks</div>
    <div class="tag tiny">Network Solutions</div>
    <div class="script">Thank You!</div>
    <svg width="295" height="40" viewBox="0 0 295 40" aria-hidden="true">
      <defs><linearGradient id="swoosh" x1="0" x2="1"><stop offset="0" stop-color="#0e2e6a"/><stop offset="1" stop-color="#6c9be0"/></linearGradient></defs>
      <path d="M0 30 Q150 0 295 18 L295 40 L0 40 Z" fill="url(#swoosh)"/>
    </svg>
  </section>

  <section class="piece envelope">
    <svg width="408" height="108" viewBox="0 0 408 108" aria-hidden="true">
      <path d="M0 0 L204 60 L408 0" fill="none" stroke="#e4e8ee" stroke-width="1"/>
    </svg>
    <div class="brand"><span class="dot"></span>Torvan Networks</div>
    <div class="addr tiny">71523 Birch Ridge Court, Suite 204<br>Sterling, VA 20783</div>
    <div class="band"></div>
  </section>

  <section class="piece sig sig-a">
    <div class="name">Brent Oakley</div>
    <div class="brand"><span class="dot"></span>Torvan Networks</div>
    <div class="tiny">BrentO@torvannetworks.example</div>
  </section>
  <section class="piece sig sig-b">
    <div class="name">Brent Oakley</div>
    <div class="tiny">555 010 2040<br>Chat: torvan.example</div>
  </section>
  <section class="piece sig sig-c">
    <div class="brand"><span class="dot"></span>Torvan Networks</div>
    <div class="tiny">www.torvannetworks.example</div>
  </section>
  <section class="piece sig sig-d">
    <div class="name">Brent Oakley</div>
    <div class="brand"><span class="dot"></span>Torvan Networks</div>
  </section>
  <section class="piece sig sig-e">
    <div class="name">Brent Oakley</div>
    <div class="tiny">555 010 2040<br>BrentO@torvannetworks.example<br>www.torvannetworks.example</div>
  </section>

  <section class="piece logo-panel">
    <div class="brand"><span class="dot"></span>Torvan Networks</div>
  </section>

</main>
</body>
</html>
```